Retail Label Design - Hand Sanitizer

LUMORA is Holvane Canadas legacy brand. For decades Holvane Canada has been trusted by our customers to provide unmatched capability in the revitalization of surfaces and materials. We are proud to relaunch LUMORATM with the same promise, but oriented towards a new challenge: meeting the demand for solutions to aid in our collective fight against COVID-19.

LUMORATM Ethanol Hand Sanitizer is the first official relaunch product – and 80% alcohol based sanitizer, free from fragrance and dye.

We want to maintain a cool and clean feel for the labels – reflective of the product. Ideally if we could incorporate a retro feel to the packaging, we would be very happy.

This label will need to be done to 3 different specs to suit a 235ml, 500ml and 4L package. We would like to start with the 500ml label. I have attached the dieline, (047-KAB) for the 500ml Package. I have also attached product info, logo and brand info.

The only requirements on the front panel is the logo, product name (Ethanol Gel Hand Sanitizer) and the quantity(473ml), space for barcode on back + info provided. the rest we will leave up to your expertise.

Font styles to use
Serif
Sans Serif

Requirements
Must have
• Logo
Product name
Quantity
Information on back panel provided.

```html
<!DOCTYPE html>
<html lang="en">
<head>
<meta charset="utf-8">
<title>LUMORA Hand Sanitizer Labels</title>
<link rel="stylesheet" href="https://fonts.googleapis.com/css2?family=Montserrat:wght@400;600;700;800&display=swap">
<style>
  :root {
    --navy: #073d5a;
    --orange: #ef8049;
    --teal: #98d6d3;
    --white: #ffffff;
    --backdrop: #d3d3d3;
  }
  * { margin: 0; padding: 0; box-sizing: border-box; }
  html, body { width: 1200px; height: 720px; overflow: hidden; }
  body {
    background: var(--backdrop);
    font-family: "Montserrat", Arial, sans-serif;
    color: var(--navy);
    position: relative;
  }
  .label {
    position: absolute;
    top: 103px;
    height: 514px;
    background: var(--white);
    overflow: hidden;
    box-shadow: 6px 8px 10px rgba(0,0,0,0.28);
  }
  .label--one { left: 0; width: 393px; z-index: 1; }
  .label--two { left: 393px; width: 382px; z-index: 2; }
  .label--three { left: 775px; width: 382px; z-index: 3; }
  .label__shapes { position: absolute; inset: 0; width: 100%; height: 100%; }
  .label__shapes .band-orange { fill: var(--orange); }
  .label__shapes .band-navy { fill: var(--navy); }
  .label__shapes .wedge { fill: var(--teal); }

  .line {
    position: absolute;
    left: 0;
    white-space: nowrap;
    line-height: 1;
    transform: translate(-50%, -50%);
  }
  .brand-name {
    font-weight: 800;
    font-size: 44px;
    letter-spacing: 1px;
    color: var(--navy);
  }
  .title { font-weight: 700; }
  .gel { font-weight: 400; }
  .claim { font-weight: 400; font-size: 17px; }
  .strength {
    position: absolute;
    display: flex;
    align-items: center;
    gap: 7px;
    color: var(--white);
    transform: translate(-50%, -50%);
  }
  .strength__value { font-weight: 800; font-size: 38px; line-height: 1; }
  .strength__words { font-weight: 600; font-size: 13px; line-height: 1.2; }
  .free-from { color: var(--white); font-size: 17px; font-weight: 400; transform: translate(-100%, -50%); }
  .volume { font-weight: 600; font-size: 26px; }
</style>
</head>
<body>

  <!-- Label variant one -->
  <section class="label label--one">
    <svg class="label__shapes" viewBox="0 0 393 514" preserveAspectRatio="none" aria-hidden="true">
      <rect class="band-orange" x="0" y="353" width="393" height="35"/>
      <rect class="band-navy" x="0" y="388" width="393" height="126"/>
      <polygon class="wedge" points="393,130 393,514 271,514"/>
    </svg>
    <div class="line brand-name" style="left:218px; top:105px;">LUMORA</div>
    <div class="line title" style="left:201px; top:207px; font-size:24px;">HAND SANITIZER</div>
    <div class="line title" style="left:201px; top:241px; font-size:24px;">ANTISEPTIQUE</div>
    <div class="line title" style="left:201px; top:270px; font-size:24px;">POUR LES MAINS</div>
    <div class="line gel" style="left:201px; top:299px; font-size:24px;">Gel</div>
    <div class="line claim" style="left:201px; top:328px;">kills 99.9% of germs</div>
    <div class="strength" style="left:201px; top:371px;">
      <span class="strength__value">70%</span>
      <span class="strength__words">Alcohol<br>d’alcool</span>
    </div>
    <div class="line free-from" style="left:268px; top:484px;">perfume and dye free</div>
    <div class="line volume" style="left:327px; top:481px;">473ml</div>
  </section>

  <!-- Label variant two -->
  <section class="label label--two">
    <svg class="label__shapes" viewBox="0 0 382 514" preserveAspectRatio="none" aria-hidden="true">
      <rect class="band-orange" x="0" y="353" width="382" height="35"/>
      <rect class="band-navy" x="0" y="388" width="382" height="126"/>
      <polygon class="wedge" points="382,130 382,514 260,514"/>
    </svg>
    <div class="line brand-name" style="left:207px; top:105px;">LUMORA</div>
    <div class="line title" style="left:190px; top:224px; font-size:16px;">HAND SANITIZER</div>
    <div class="line title" style="left:190px; top:248px; font-size:16px;">ANTISEPTIQUE POUR LES MAINS</div>
    <div class="line gel" style="left:190px; top:278px; font-size:24px;">Gel</div>
    <div class="line claim" style="left:190px; top:315px;">kills 99.9% of germs</div>
    <div class="strength" style="left:190px; top:371px;">
      <span class="strength__value">70%</span>
      <span class="strength__words">Alcohol<br>d’alcool</span>
    </div>
    <div class="line free-from" style="left:257px; top:484px;">perfume and dye free</div>
    <div class="line volume" style="left:316px; top:481px;">473ml</div>
  </section>

  <!-- Label variant three -->
  <section class="label label--three">
    <svg class="label__shapes" viewBox="0 0 382 514" preserveAspectRatio="none" aria-hidden="true">
      <rect class="band-orange" x="0" y="353" width="382" height="35"/>
      <rect class="band-navy" x="0" y="388" width="382" height="126"/>
      <polygon class="wedge" points="382,130 382,514 260,514"/>
    </svg>
    <div class="line brand-name" style="left:207px; top:105px;">LUMORA</div>
    <div class="line title" style="left:190px; top:221px; font-size:29px;">HAND SANITIZER</div>
    <div class="line title" style="left:190px; top:248px; font-size:16px;">ANTISEPTIQUE POUR LES MAINS</div>
    <div class="line gel" style="left:190px; top:280px; font-size:27px;">Gel</div>
    <div class="line claim" style="left:190px; top:315px;">kills 99.9% of germs</div>
    <div class="strength" style="left:190px; top:371px;">
      <span class="strength__value">70%</span>
      <span class="strength__words">Alcohol<br>d’alcool</span>
    </div>
    <div class="line free-from" style="left:257px; top:484px;">perfume and dye free</div>
    <div class="line volume" style="left:316px; top:481px;">473ml</div>
  </section>

</body>
</html>
```